Real Estate Business Cards

Looking for a clean, sharp and professional look for our Real Estate investment Fund that invests in Multi Family Apartment buildings.

Target Market(s)

Real Estate Fund

Industry/Entity Type

Real Estate

Contact Information for Business Card

Company Description: Real Estate Investment Fund
Company Name: RKW Holdings
Name: Marcus Olvane
Cell: (917) 482-0657
Email: marcus@rkwholdings-example.com
Website: www.rkwholdings-example.com
Address: 418, 9th Street, Brooklyn NY 11218

Colors

Designer to choose colors to be used in the design.

Requirements
Nice to have
• Colors to match logo

```html
<!DOCTYPE html>
<html lang="en">
<head>
<meta charset="utf-8">
<title>RKW Holdings – Business Card</title>
<link href="https://fonts.googleapis.com/css2?family=Lato:wght@400;700&display=swap" rel="stylesheet">
<style>
  :root {
    --brand-blue: #1a75b0;
    --brand-blue-deep: #0d4b8e;
    --ink: #1d1d1d;
    --slate: #4a4a4c;
    --paper: #ffffff;
    --haze-light: #f2f2f2;
    --haze-mid: #d6d6d6;
    --haze-dark: #b9b9b9;
  }
  * { margin: 0; padding: 0; box-sizing: border-box; }
  html, body {
    width: 1200px; height: 1200px; overflow: hidden;
    background: var(--paper);
    font-family: "Lato", sans-serif;
  }
  .canvas { position: relative; width: 1200px; height: 1200px; }

  /* Front */
  .card-front {
    position: absolute; left: 106px; top: 56px;
    width: 992px; height: 511px; overflow: hidden;
  }
  .skyline-photo {
    position: absolute; inset: 0;
    background: linear-gradient(180deg, var(--haze-light) 0%, #e6e6e6 40%, var(--haze-mid) 62%, var(--haze-dark) 100%);
  }
  .front-arc { position: absolute; inset: 0; }
  .front-brand {
    position: absolute; left: 0; right: 0; top: 262px;
    display: flex; justify-content: center; align-items: center; gap: 18px;
  }
  .brand-square { width: 34px; height: 34px; background: var(--brand-blue); }
  .brand-name {
    font-weight: 400; color: var(--slate); letter-spacing: 3px;
    text-transform: uppercase;
  }
  .front-brand .brand-name { font-size: 50px; }
  .tagline {
    position: absolute; left: 0; right: 0; top: 437px;
    text-align: center; color: var(--paper);
    font-size: 22px; font-weight: 400; letter-spacing: 0.3px;
  }

  /* Back */
  .card-back {
    position: absolute; left: 106px; top: 594px;
    width: 992px; height: 541px; overflow: hidden;
    background: var(--paper);
  }
  .skyline-faint {
    position: absolute; left: 0; right: 0; bottom: 0; height: 150px;
    background: linear-gradient(180deg, rgba(230,230,230,0) 0%, #ececec 35%, #e2e2e2 100%);
  }
  .back-brand {
    position: absolute; left: 28px; top: 76px;
    display: flex; align-items: center; gap: 16px;
  }
  .back-brand .brand-square { width: 40px; height: 40px; }
  .back-brand .brand-name { font-size: 32px; }
  .contact {
    position: absolute; left: 0; right: 0; text-align: center;
  }
  .person-name {
    top: 142px; font-size: 38px; font-weight: 700; color: var(--brand-blue);
  }
  .person-role { top: 196px; font-size: 20px; color: var(--ink); }
  .icon-row {
    position: absolute; left: 0; right: 0; top: 241px;
    display: flex; justify-content: center; gap: 28px;
  }
  .icon-row svg { width: 48px; height: 48px; }
  .contact-line { font-size: 28px; color: var(--ink); }
  .phone { top: 306px; }
  .email { top: 357px; }
  .web { top: 404px; }
  .address { top: 447px; }
</style>
</head>
<body>
<main class="canvas">

  <section class="card-front">
    <div class="skyline-photo" role="img" aria-label="Hazy grey aerial photograph of a city skyline with tall towers"></div>
    <svg class="front-arc" viewBox="0 0 992 511" aria-hidden="true">
      <path d="M0,450 Q496,294 992,450 L992,511 L0,511 Z" fill="var(--brand-blue-deep)"/>
      <path d="M0,472 Q496,306 992,474 L992,511 L0,511 Z" fill="var(--brand-blue)"/>
      <polygon points="278,453 342,449 342,457" fill="var(--paper)"/>
      <polygon points="656,449 720,453 656,457" fill="var(--paper)"/>
    </svg>
    <div class="front-brand">
      <span class="brand-square" aria-hidden="true"></span>
      <span class="brand-name">RKW Holdings</span>
    </div>
    <p class="tagline">Real Estate Investment Fund</p>
  </section>

  <section class="card-back">
    <div class="skyline-faint" role="img" aria-label="Faint grey city skyline silhouette"></div>
    <div class="back-brand">
      <span class="brand-square" aria-hidden="true"></span>
      <span class="brand-name">RKW Holdings</span>
    </div>
    <h1 class="contact person-name">Marcus Olvane</h1>
    <p class="contact person-role">Owner</p>

    <div class="icon-row" aria-hidden="true">
      <svg viewBox="0 0 48 48">
        <circle cx="24" cy="24" r="22" fill="var(--brand-blue)" stroke="#123a5c" stroke-width="2"/>
        <path d="M15,14 l5,-2 l4,7 l-3,3 q2,5 7,7 l3,-3 l7,4 l-2,5 q-12,1 -21,-21 z" fill="var(--paper)"/>
      </svg>
      <svg viewBox="0 0 48 48">
        <circle cx="24" cy="24" r="22" fill="var(--brand-blue)" stroke="#123a5c" stroke-width="2"/>
        <rect x="13" y="16" width="22" height="16" fill="var(--paper)"/>
        <path d="M13,16 L24,25 L35,16 M13,32 L21,23 M35,32 L27,23" fill="none" stroke="var(--brand-blue)" stroke-width="1.6"/>
      </svg>
      <svg viewBox="0 0 48 48">
        <circle cx="24" cy="24" r="22" fill="var(--brand-blue)" stroke="#123a5c" stroke-width="2"/>
        <circle cx="24" cy="24" r="12" fill="var(--paper)"/>
        <ellipse cx="24" cy="24" rx="5" ry="12" fill="none" stroke="var(--brand-blue)" stroke-width="1.6"/>
        <path d="M12,24 H36 M14,18 H34 M14,30 H34" stroke="var(--brand-blue)" stroke-width="1.6"/>
      </svg>
      <svg viewBox="0 0 48 48">
        <circle cx="24" cy="24" r="22" fill="var(--brand-blue)" stroke="#123a5c" stroke-width="2"/>
        <path d="M24,12 a8,8 0 0 1 8,8 c0,6 -8,12 -8,12 c0,0 -8,-6 -8,-12 a8,8 0 0 1 8,-8 z" fill="var(--paper)"/>
        <circle cx="24" cy="20" r="3.2" fill="var(--brand-blue)"/>
        <path d="M14,36 L18,31 H30 L34,36 Z" fill="var(--paper)"/>
      </svg>
    </div>

    <p class="contact contact-line phone">(917) 482-0657</p>
    <p class="contact contact-line email">marcus@rkwholdings-example.com</p>
    <p class="contact contact-line web">www.rkwholdings-example.com</p>
    <p class="contact contact-line address">418, 9th Street, Brooklyn NY 11218</p>
  </section>

</main>
</body>
</html>
```